Wedding Invitation Design Project

I need a wedding invitation designed.

The language will be in Turkish, I will send the full translated text of the selected design.

Here are some details that might be useful:
Getting married: Emre Tandoğan (Groom) and Derya Oltuner (Bride)
Derya will be changing last name to Tandoğan and drop Oltuner.

We first met in May 21 2011 (blind date set up by close friends)
Proposal was in May 20 2012 (one year including the leap day :-))
Engagement date July 14 2012 (don't really have to include in design, but up to you)
Wedding date December 22 2012
Wedding location: Selvirose Hotel - Levent, Istanbul
Invitees: 250-300 people - personal friends (aged 24-31), family and their friends (aged 40 and up mostly)
Updates

Just uploaded some sample invites to give some directions for submissions.

Also please note that this is the actual invitation itself, therefore should contain location, time and date and RSVP contacts as well.

Hi,

Sorry for the delayed response.  It has been a crazy week of engagement party preparations.

The designs that you have submitted all look very promising... I was worried at the beginning but now I'm sure that our invitation will be one of these.

I will extend the deadline another two weeks and provide detailed feedback about all the designs before Monday.

Thank you all for your efforts and patience,

Kind Regards,
Emre

Reason: I'll be posting detailed comments about every design by Monday. As well as Turkish wordings... (The grammar rules will probably change the layouts in most cases).

Hi all..

I uploaded one more file inspiration.pptx.. you can take design cues from the images in it..

A couple of more details:
Our first blind date, we went to a jazz concert.
I'm a cat person and she's a dog person.

fyi..

looking forward to all the designs..

Regards,
Emre

Reason: Sorry for the late responses in the last couple of days. I'll be providing detailed feedback for all designs later today.

Reason: Again.. sorry for delayed comments on designs.. I've been swamped with work this week.. (literally leaving the office at midnight most days).. I will send detailed comments sometime this weekend.. Please hang in there..

Wedding

Requirements
Must have
• The following details must be included in the text:
Date and location of the wedding
RSVP date and phone number (just use a dummy number & date for now)

The fonts used in the design must support Turkish characters both in lower case and upper case: http://en.lexipedora.org/wiki/Lexipedora:Turkish_characters

Must have image(s)/icon(s) etc. A text only approach will not be acceptable.

Images that look like they came out of Quillora Pages's clip-art gallery will not be acceptable either.
Nice to have
• This is a fantastic example:
http://www.veronikastraub.com/Irma-Hugo-Invites

These can also offer some inspiration: http://www.yayweretyingtheknot.com/2011/11/tuesday-top-10-awesome-infographic-wedding-invitations/

I'm not firm on this, but the less color there is, the better.

If you are using letter-press etc methods, please let me know if you can get them printed and shipped to Turkey. I can pay for these services separately
Should not have
• Should be printable on regular paper without having fold or cut in irregular shapes. (1 or 2 folds to make an envelop shape is OK.)
Should not be larger than 20cm on either side.
Should not have small print (many older invitees)
No religious themes of any kind or affiliation.

```html
<!DOCTYPE html>
<html lang="en">
<head>
<meta charset="UTF-8">
<title>Wedding Invitation – Emre Tandoğan and Derya Oltuner</title>
<link rel="stylesheet" href="https://fonts.googleapis.com/css2?family=Delius&family=Gochi+Hand&display=swap">
<style>
  :root {
    --paper: #ffffff;
    --ink: #111111;
    --pink: #e2127f;
    --frame: #9a9a9a;
    --art-light: #f1f1f1;
    --art-mid: #d6d6d6;
  }
  * { margin: 0; padding: 0; box-sizing: border-box; }
  html, body {
    width: 1194px;
    height: 1200px;
    overflow: hidden;
    background: var(--paper);
  }
  .invitation {
    position: relative;
    width: 1194px;
    height: 1200px;
    background: var(--paper);
    font-family: "Delius", "Comic Sans MS", cursive;
    color: var(--ink);
  }
  .frame {
    position: absolute;
    inset: 7px;
    border: 2px solid var(--frame);
  }
  .abs { position: absolute; }
  .centered { transform: translateX(-50%); white-space: nowrap; text-align: center; }

  .story-heading { top: 48px; font-size: 28px; }
  .story-caption { top: 333px; font-size: 26px; }

  .illustration {
    background: radial-gradient(ellipse at center, var(--art-mid) 0%, var(--art-light) 70%, var(--paper) 100%);
    border-radius: 40px;
  }
  .illustration--first-meeting { left: 28px; top: 92px; width: 472px; height: 214px; }
  .illustration--proposal { left: 770px; top: 90px; width: 328px; height: 222px; }

  .scribble {
    font-family: "Gochi Hand", "Comic Sans MS", cursive;
    color: var(--pink);
    white-space: nowrap;
    line-height: 1;
  }
  .scribble--later { left: 522px; top: 258px; font-size: 46px; transform: rotate(4deg); }
  .scribble--now { left: 985px; top: 440px; font-size: 54px; transform: rotate(-22deg); }
  .scribble--when { left: 72px; top: 772px; font-size: 46px; transform: rotate(14deg); }
  .scribble--where { left: 1020px; top: 812px; font-size: 46px; transform: rotate(-40deg); }

  .arrows { position: absolute; left: 0; top: 0; width: 1194px; height: 1200px; pointer-events: none; }
  .arrows path { fill: none; stroke: var(--ink); stroke-width: 3.5; stroke-linecap: round; stroke-linejoin: round; }

  .headline { left: 597px; top: 420px; font-size: 58px; }
  .couple-name { left: 594px; color: var(--pink); font-size: 64px; }
  .couple-name--groom { top: 516px; }
  .couple-joiner { top: 614px; }
  .couple-name--bride { top: 710px; }

  .event-date { left: 597px; top: 822px; font-size: 60px; }
  .event-venue { left: 597px; top: 908px; font-size: 42px; }

  .rsvp { left: 597px; color: var(--pink); font-size: 43px; }
  .rsvp--deadline { top: 1028px; }
  .rsvp--contact { top: 1094px; }
</style>
</head>
<body>
<main class="invitation">
  <div class="frame"></div>

  <p class="abs centered story-heading" style="left:264px;">We first met in May 21, 2011</p>
  <p class="abs centered story-heading" style="left:913px;">Proposal was in May 20, 2012</p>

  <div class="abs illustration illustration--first-meeting" role="img" aria-label="Hand-drawn stick-figure couple and their two friends meeting on a blind date"></div>
  <div class="abs illustration illustration--proposal" role="img" aria-label="Hand-drawn stick-figure groom kneeling to propose to the bride with a small heart"></div>

  <p class="abs centered story-caption" style="left:264px;">(blind date set up by close friends)</p>
  <p class="abs centered story-caption" style="left:913px;">(one year including the leap day :-))</p>

  <svg class="arrows" viewBox="0 0 1194 1200" aria-hidden="true">
    <!-- story arrow -->
    <path d="M543 205 L662 205 M606 172 L664 205 L608 238"/>
    <!-- now arrow -->
    <path d="M1040 426 L858 452 L918 420 M858 452 L918 478"/>
    <!-- when arrow -->
    <path d="M132 750 L300 826 M262 776 L302 826 L238 830"/>
    <!-- where arrow -->
    <path d="M1076 760 L944 888 M944 830 L944 888 L1000 888"/>
  </svg>

  <span class="abs scribble scribble--later">Later</span>
  <span class="abs scribble scribble--now">NOW</span>
  <span class="abs scribble scribble--when">When</span>
  <span class="abs scribble scribble--where">Where</span>

  <h1 class="abs centered headline" style="font-weight:400;">Getting married:</h1>
  <p class="abs centered couple-name couple-name--groom">Emre Tandoğan</p>
  <p class="abs centered couple-name couple-joiner">and</p>
  <p class="abs centered couple-name couple-name--bride">Derya Oltuner</p>

  <p class="abs centered event-date">December 22, 2012</p>
  <p class="abs centered event-venue">Selvirose Hotel - Levent, Istanbul</p>

  <p class="abs centered rsvp rsvp--deadline">Please tell us your going by October 30, 2012</p>
  <p class="abs centered rsvp rsvp--contact">(Because we know you are:-)) Call: 555.555.555</p>
</main>
</body>
</html>
```